Online video and marketing company business cards

Need to get some new business cards designed to fit with our new logo. The cards should be professional, clean and simple.

Cards should have:

Name
Position
2 line address
telephone
mobile
email address
web address

We need to have our logo and if possible say what we do...
ONLINE FILM PRODUCTION & STRATEGY

Marketing

```html
<!DOCTYPE html>
<html lang="en">
<head>
<meta charset="utf-8">
<title>Vistareel – Business Card</title>
<link rel="stylesheet" href="https://fonts.googleapis.com/css2?family=Poiret+One&display=swap">
<style>
  :root {
    --page-bg: #ffffff;
    --card-light: #ffffff;
    --card-edge: #cfd1d3;
    --brand-teal: #4aa0bf;
    --brand-navy: #1f4a6f;
    --text-ink: #2d4c6c;
  }
  * { margin: 0; padding: 0; box-sizing: border-box; }
  html, body {
    width: 958px;
    height: 1200px;
    overflow: hidden;
    background: var(--page-bg);
  }
  .canvas {
    position: relative;
    width: 958px;
    height: 1200px;
  }
  .business-card {
    position: absolute;
    left: 162px;
    top: 413px;
    width: 634px;
    height: 374px;
    background: radial-gradient(ellipse 75% 85% at 45% 35%, var(--card-light) 0%, #eeeff0 45%, var(--card-edge) 100%);
    font-family: "Poiret One", sans-serif;
    color: var(--text-ink);
  }
  .brand-mark {
    position: absolute;
    left: 43px;
    top: 37px;
    width: 78px;
    height: 78px;
  }
  .brand-name {
    position: absolute;
    left: 135px;
    top: 48px;
    font-size: 66px;
    line-height: 1;
    color: var(--brand-teal);
    letter-spacing: 1px;
    white-space: nowrap;
  }
  .brand-tagline {
    position: absolute;
    left: 137px;
    top: 134px;
    font-size: 16px;
    letter-spacing: 0.2px;
    color: var(--brand-navy);
    white-space: nowrap;
  }
  .person {
    position: absolute;
    left: 0;
    width: 634px;
    text-align: center;
    top: 205px;
  }
  .person-name {
    font-size: 26px;
    line-height: 30px;
    color: var(--brand-navy);
  }
  .person-role {
    font-size: 18px;
    line-height: 26px;
  }
  .contact {
    position: absolute;
    top: 316px;
    font-size: 15px;
    line-height: 20px;
    white-space: nowrap;
  }
  .contact-address { left: 27px; }
  .contact-phones { left: 210px; }
  .contact-online { right: 27px; text-align: right; }
</style>
</head>
<body>
<main class="canvas">
  <section class="business-card" aria-label="Business card">
    <svg class="brand-mark" viewBox="0 0 78 78" aria-hidden="true">
      <circle cx="39" cy="39" r="36" fill="none" stroke="var(--brand-navy)" stroke-width="6"/>
    </svg>
    <div class="brand-name">vistareel</div>
    <div class="brand-tagline">ONLINE FILM PRODUCTION &amp; STRATEGY</div>

    <div class="person">
      <div class="person-name">John Doe</div>
      <div class="person-role">Production manager</div>
    </div>

    <address class="contact contact-address" style="font-style:normal">
      14, Harlow Mews<br>
      London E2 7QP U.K.
    </address>
    <div class="contact contact-phones">
      +44(0)207 946 0321<br>
      +44(0)207 946 0321
    </div>
    <div class="contact contact-online">
      john.doe@vistareel.com<br>
      www.vistareel.com
    </div>
  </section>
</main>
</body>
</html>
```